VELORA Group Fitness Class Launch Poster!

We need a poster design for a upcoming Group Fitness Class launch with two additional social media post designs.
Please follow our Brand Style Guide, as I will not be able to accept anything outside of this guide.
Class Description:
Come and VELORA your body with this class while catching up with friends and meeting new people. It is low-impact strength training with bodyweight exercises to help improve muscular strength, cardiovascular endurance, balance, bone health and functional training. It is suitable for all fitness levels.
Class Length: 30 Minutes
Intro script for class online:
📣New class alert❗
TPW team is excited to announce the launch of our new class, "VELORA", instructed by Jo! 🥰
Unsure if group fitness classes are for you? Join us for 30-minute low-impact strength training with bodyweight exercises! It's time to build your confidence in a fun and supportive environment.
Target Market(s)
Target audience is mostly females which barrier to entry to fitness is not having the confidence to join or has limited capability and needing low impact. Important to note that our demographic tends to be below 50... So barriers is most likely to be confidence, overweight or unfit.
Industry/Entity Type
Fitness
Other font styles liked:
- Please follow the Style Guide Fonts.
Requirements
Must have
- The project must follow our Brand Guidelines & include the class logo. Poster should be exciting and stand out. Don't necessarily have to use the stock images provided.
Should not have
- If you select your own image, the preference would be that it does not only include slim/fit looking individuals.

```html
<!DOCTYPE html>
<html lang="en">
<head>
<meta charset="utf-8">
<title>VELORA Class Launch Poster</title>
<link rel="stylesheet" href="https://fonts.googleapis.com/css2?family=Noto+Serif:wght@400;700&family=Open+Sans:ital,wght@0,400;0,600;1,600&display=swap">
<style>
  :root {
    --brand-red: #a8192e;
    --brand-salmon: #d2605a;
    --brand-grey: #c8c3c1;
    --ink: #141414;
    --paper: #ffffff;
    --backdrop: #e9e9e9;
    --photo-dark: #2a2d31;
    --photo-mid: #4b4f55;
  }
  * { box-sizing: border-box; margin: 0; padding: 0; }
  html, body { width: 1200px; height: 1177px; overflow: hidden; }
  body { background: var(--backdrop); position: relative; font-family: "Open Sans", sans-serif; }

  .poster {
    position: absolute; left: 246px; top: 78px; width: 734px; height: 1040px;
    background: var(--paper);
  }
  .block { position: absolute; }

  .alert-title {
    left: 0; top: 0; width: 368px; height: 102px; background: var(--brand-red);
    color: var(--paper); font-family: "Noto Serif", serif; font-weight: 700;
    font-size: 38px; line-height: 40px; text-align: center; padding-top: 12px;
  }
  .alert-sub {
    left: 0; top: 102px; width: 368px; height: 96px; background: var(--brand-salmon);
    color: var(--paper); font-family: "Noto Serif", serif; font-weight: 700;
    font-size: 17.5px; line-height: 23px; text-align: center; padding-top: 14px;
  }
  .brand-mark {
    left: 368px; top: 0; width: 366px; height: 198px;
    display: flex; align-items: center; justify-content: center; gap: 12px;
  }
  .brand-dot { width: 22px; height: 22px; border-radius: 50%; background: var(--brand-red); }
  .brand-name {
    font-family: "Noto Serif", serif; font-weight: 400; font-size: 30px;
    line-height: 34px; color: var(--ink);
  }

  .hero-photo {
    left: 0; top: 204px; width: 734px; height: 402px;
    background: radial-gradient(ellipse at 50% 45%, var(--photo-mid) 0%, var(--photo-dark) 75%);
  }
  .class-mark {
    left: 0; top: 480px; width: 368px; height: 126px; background: #f3f2f1;
    display: flex; align-items: center; justify-content: center;
  }
  .class-name {
    font-family: "Noto Serif", serif; font-weight: 700; font-size: 56px;
    letter-spacing: 2px; color: var(--ink);
  }

  .info-length, .info-instructor {
    top: 606px; height: 40px; font-family: "Noto Serif", serif; font-weight: 700;
    font-size: 18px; display: flex; align-items: center; justify-content: center;
  }
  .info-length { left: 0; width: 368px; background: var(--ink); color: var(--paper); }
  .info-instructor { left: 368px; width: 366px; background: var(--brand-grey); color: var(--ink); }

  .class-details {
    left: 0; top: 650px; width: 734px; height: 300px; background: var(--brand-red);
    color: var(--paper); text-align: center; padding-top: 26px;
  }
  .details-lead {
    font-family: "Noto Serif", serif; font-weight: 700; font-size: 20px; line-height: 26px;
  }
  .details-body { font-size: 14.5px; line-height: 22px; margin-top: 16px; }
  .details-question { font-style: italic; font-weight: 600; font-size: 14.5px; margin-top: 22px; }
  .details-cta {
    font-family: "Noto Serif", serif; font-weight: 700; font-size: 21px; line-height: 27px; margin-top: 10px;
  }

  .tagline-confidence {
    left: 0; top: 956px; width: 368px; height: 84px; text-align: center; padding-top: 16px;
    font-family: "Noto Serif", serif; font-weight: 700;
  }
  .tagline-confidence .small { font-size: 18px; line-height: 22px; color: var(--ink); }
  .tagline-confidence .large { font-size: 33px; line-height: 38px; color: var(--brand-red); }
  .tagline-environment {
    left: 372px; top: 956px; width: 362px; height: 84px; background: var(--brand-grey);
    text-align: center; padding-top: 16px; font-family: "Noto Serif", serif; font-weight: 700;
  }
  .tagline-environment .small { font-size: 18px; line-height: 22px; color: var(--brand-red); }
  .tagline-environment .large { font-size: 29px; line-height: 36px; color: var(--ink); }
</style>
</head>
<body>
  <main class="poster">
    <h1 class="block alert-title">NEW CLASS<br>ALERT</h1>
    <p class="block alert-sub">TPW TEAM IS EXCITED TO<br>ANNOUNCE THE LAUNCH<br>OF OUR NEW CLASS</p>
    <div class="block brand-mark">
      <span class="brand-dot"></span>
      <span class="brand-name">Harlow Vale<br>Recreation &amp; Fitness</span>
    </div>

    <div class="block hero-photo" role="img" aria-label="Photo of three people of varied body types doing bodyweight squats together in a dark gym"></div>
    <div class="block class-mark"><span class="class-name">VELORA</span></div>

    <div class="block info-length">CLASS LENGTH: 30 MINS</div>
    <div class="block info-instructor">INSTRUCTED BY JO</div>

    <section class="block class-details">
      <p class="details-lead">Come and VELORA your body with this class<br>while catching up with friends &amp; meeting new people.</p>
      <p class="details-body">It is low-impact strength training with bodyweight exercises to help improve<br>muscular strength, cardiovascular endurance, balance, bone health and functional training.<br>It is suitable for all fitness levels.</p>
      <p class="details-question">Unsure if group fitness classes are for you?</p>
      <p class="details-cta">Join us for 30-minute low-impact<br>strength training with bodyweight exercises!</p>
    </section>

    <div class="block tagline-confidence">
      <div class="small">IT’S TIME TO BUILD YOUR</div>
      <div class="large">CONFIDENCE</div>
    </div>
    <div class="block tagline-environment">
      <div class="small">IN A FUN &amp; SUPPORTIVE</div>
      <div class="large">ENVIRONMENT</div>
    </div>
  </main>
</body>
</html>
```